Web Design needed for logo design project

I am needing an interactive website for BC. Talvor Care Management is a nationwide company that combines the front desk administrative operation within Professional offices (Dental, Chiropractic, Optometry). I am needing a website designed that will provide information for potential new clients that are interested in joining our company to provide to them administrative support. I need a design for the marketing material within the folder, I will add content later. I am looking for clean crisp professional. No dancing teeth, hearts, or EKG signals please. We need it to appeal to 27-40 years old professionals. The professions are equally divided at 50/50 female to male. I already have a logo, it will be attached.
Updates

Target Market(s)

We need it to appeal to 27-40 years old professionals. The professions are equally divided at 50/50 female to male. I already have a logo, it will be attached.

Industry/Entity Type

Marketing

Requirements
Must have
• Needs to be in Word Press. It must have scalability to various screen sizes (Monitor, Phone screen, IPad, etc). Must have a customer portal capability, so professionals can access their information through a portal on the website. Have the capability to run a practice calculator or view a video requiring that it captures the visitors information so I can contact them regarding their interest in the site. Needs to have links to social media.

```html
<!DOCTYPE html>
<html lang="en">
<head>
<meta charset="utf-8">
<title>Talvor Care Management</title>
<link rel="stylesheet" href="https://fonts.googleapis.com/css2?family=PT+Sans:wght@400;700&family=Arimo:wght@400;700&display=swap">
<style>
  :root {
    --white: #ffffff;
    --brand-navy: #1f4f8f;
    --sky: #42b1e6;
    --ocean: #0a7fcf;
    --indigo: #2f56a6;
    --nav-text: #6d6d6d;
    --ink: #2b2b2b;
    --muted: #6b6b6b;
    --band: #f6f6f6;
    --divider: rgba(255,255,255,0.25);
  }
  * { box-sizing: border-box; margin: 0; padding: 0; }
  html, body { width: 1200px; height: 898px; overflow: hidden; background: var(--white); }
  body { position: relative; font-family: "Arimo", Arial, sans-serif; color: var(--ink); }

  .site-header { position: absolute; left: 0; top: 0; width: 1200px; height: 139px; background: var(--white); }
  .brand { position: absolute; left: 133px; top: 50px; display: flex; align-items: center; gap: 12px; }
  .brand-mark { width: 30px; height: 30px; background: var(--brand-navy); flex: none; }
  .brand-name { font-family: "PT Sans", sans-serif; font-weight: 700; font-size: 19px; line-height: 21px; color: var(--brand-navy); letter-spacing: 0.4px; }

  .main-nav { position: absolute; left: 403px; top: 66px; display: flex; height: 38px; }
  .main-nav a { display: flex; align-items: center; padding: 0 14px; margin-right: 15px; font-size: 12.5px; color: var(--nav-text); text-decoration: none; text-transform: uppercase; }
  .main-nav a.active { background: var(--sky); color: var(--white); }

  .hero { position: absolute; left: 0; top: 139px; width: 1200px; height: 601px; }
  .hero-photo { position: absolute; inset: 0;
    background: linear-gradient(90deg, #c9a78f 0%, #e2c9b4 25%, #dbd4d6 45%, #e9cdb8 70%, #d7b89f 100%); }
  .hero-title { position: absolute; left: 133px; top: 86px; font-family: "PT Sans", sans-serif; font-weight: 400; font-size: 63px; line-height: 64px; color: var(--white); }
  .hero-sub { position: absolute; left: 133px; top: 239px; font-family: "PT Sans", sans-serif; font-size: 20px; line-height: 31px; color: var(--white); }
  .slider { position: absolute; left: 133px; top: 376px; width: 889px; height: 1px; background: rgba(255,255,255,0.6); }
  .slider-active { position: absolute; left: 380px; top: -1px; width: 216px; height: 3px; background: var(--white); }
  .slider-index { position: absolute; left: 0; top: -18px; font-size: 11px; color: var(--white); }

  .info-cards { position: absolute; left: 133px; top: 414px; display: flex; height: 187px; }
  .card { position: relative; width: 296px; height: 187px; padding: 16px 27px; color: var(--white); }
  .card-support { background: var(--sky); }
  .card-network { background: var(--ocean); }
  .card-hours { background: var(--indigo); }
  .card h2 { font-family: "PT Sans", sans-serif; font-weight: 400; font-size: 21px; margin-bottom: 13px; }
  .card p { font-size: 11.3px; line-height: 17.5px; }
  .read-more { position: absolute; left: 27px; display: inline-block; padding: 4px 7px; border: 1px solid var(--white); font-size: 11.5px; color: var(--white); text-decoration: none; }
  .hours-list { list-style: none; margin-top: 6px; }
  .hours-list li { display: flex; justify-content: space-between; font-size: 12px; padding: 9px 0 10px; border-bottom: 1px solid var(--divider); }

  .features { position: absolute; left: 0; top: 740px; width: 1200px; height: 158px; background: var(--band); }
  .feature { position: absolute; top: 45px; display: flex; gap: 18px; }
  .feature svg { flex: none; }
  .feature h3 { font-family: "PT Sans", sans-serif; font-weight: 400; font-size: 15px; color: var(--ink); margin: 3px 0 8px; }
  .feature p { width: 205px; font-size: 11.3px; line-height: 18px; color: var(--muted); }
</style>
</head>
<body>
  <header class="site-header">
    <div class="brand"><span class="brand-mark"></span><span class="brand-name">Talvor Care<br>Management</span></div>
    <nav class="main-nav">
      <a class="active" href="#">Home</a><a href="#">Blog</a><a href="#">Pages</a><a href="#">Services</a><a href="#">Portal</a><a href="#">Gallery</a><a href="#">Contact</a>
    </nav>
  </header>

  <section class="hero">
    <div class="hero-photo" role="img" aria-label="Photo of a friendly front desk team member welcoming a visitor at a professional office"></div>
    <h1 class="hero-title">Grow your<br>practice</h1>
    <p class="hero-sub">Let our team run your front desk<br>while you focus on care</p>
    <div class="slider"><span class="slider-index">1</span><span class="slider-active"></span></div>

    <div class="info-cards">
      <article class="card card-support">
        <h2>Front Desk Support</h2>
        <p>We handle scheduling, billing and patient intake for dental, chiropractic and optometry offices nationwide.</p>
        <a class="read-more" href="#" style="top:134px">Read more &rarr;</a>
      </article>
      <article class="card card-network">
        <h2>Join Our Network</h2>
        <p>Partner offices get a dedicated admin team and a secure client portal. Try the practice calculator to see your savings.</p>
        <a class="read-more" href="#" style="top:151px">Read more &rarr;</a>
      </article>
      <article class="card card-hours">
        <h2>Opening Hours</h2>
        <ul class="hours-list">
          <li><span>Monday - Friday</span><span>8.00 - 17.00</span></li>
          <li><span>Saturday</span><span>9.30 - 17.30</span></li>
          <li><span>Sunday</span><span>9.30 - 15.00</span></li>
        </ul>
      </article>
    </div>
  </section>

  <section class="features">
    <div class="feature" style="left:133px">
      <svg width="54" height="60" viewBox="0 0 54 60"><polygon points="27,0 54,15 54,45 27,60 0,45 0,15" fill="#42b1e6"/><path d="M23 21h8M25 21v8l-5 10h14l-5-10v-8" stroke="#fff" stroke-width="2" fill="none"/></svg>
      <div><h3>Dental Offices</h3><p>Reception, recalls and insurance handled by trained staff so your chairs stay full every day.</p></div>
    </div>
    <div class="feature" style="left:438px">
      <svg width="54" height="60" viewBox="0 0 54 60"><polygon points="27,0 54,15 54,45 27,60 0,45 0,15" fill="#42b1e6"/><g fill="#fff"><circle cx="27" cy="24" r="4"/><circle cx="27" cy="36" r="4"/><circle cx="21" cy="30" r="4"/><circle cx="33" cy="30" r="4"/></g></svg>
      <div><h3>Chiropractic</h3><p>Booking, check-in and follow-up calls managed for you, with clear reports in your portal.</p></div>
    </div>
    <div class="feature" style="left:743px">
      <svg width="54" height="60" viewBox="0 0 54 60"><polygon points="27,0 54,15 54,45 27,60 0,45 0,15" fill="#42b1e6"/><path d="M21 21h12M21 39h12M22 22l10 16M32 22l-10 16" stroke="#fff" stroke-width="2" fill="none"/></svg>
      <div><h3>Optometry</h3><p>Exam scheduling, frame orders and claims kept on time, so your practice runs smoothly.</p></div>
    </div>
  </section>
</body>
</html>
```